Professional & Modern Technology Business Card

We need a business card for our software/technology firm. Our services include Program/Project Management, Project Controls and Enterprise Analytics. Our clients are usually in the Aviation, Public Works, Transportation and Electric & Water Utility industries. We serve both public and private clients. Would like a very professional, conservative but somewhat modern design. Design, Develop, Deploy is the corporate tagline. We have two offices. The headquarters is in Atlanta, GA and a satellite office In Savannah, GA. Corporate Logo Attached.
Looking to do website and corporate brochure after the successful completion of this project. Would like to begin a working relationship with best designers.
Tagline: Design, Develop, Deploy
Website: www.quelvanesystems.example
My Name: Marla Dunstead
My Title: CEO
Email: mdunstead@quelvanesystems.example
Atlanta Address:
87 Corliss Avenue, #2291
Atlanta, GA 30301
Office: 404.555.0182
Fax: 404.555.0147
Mobile: 404.555.0163
Savannah Address:
350 West Harrow Bend Road
Suite 720
Savannah, GA 31401
Office: 912.555.0139
Fax: 404.555.0147
Mobile: 404.555.0163
Updates
Please include the email address in your designs: mdunstead@quelvanesystems.example.
I appreciate everyone's design efforts. Just a few notes:
1. Please remove the mobile number from the cards
2. The backs of the cards can be utilized for writing notes. Make sure your design on the back of the card is conducive to clearly adding writing if needed.
3. No black backgrounds please
4. Only use the corporate logo on the front of the card. You can use portions of the logo design, but not the logo in totality.
Thank You
Industry/Entity Type
Conservative
Look and feel
Each slider illustrates characteristics of the customer's brand and the style your logo design should communicate.

```html
<!DOCTYPE html>
<html lang="en">
<head>
<meta charset="utf-8">
<title>Quelvane Systems — Business Card</title>
<link rel="stylesheet" href="https://fonts.googleapis.com/css2?family=Orbitron:wght@700&family=PT+Sans:ital,wght@0,400;0,700;1,700&display=swap">
<style>
  :root {
    --stage: #ece8e2;
    --card: #ffffff;
    --blue: #1b8fd0;
    --green: #8cc63f;
    --yellow: #e3c21f;
    --ink: #111111;
    --muted: #444444;
    --footer: #e9eef2;
    --on-color: #ffffff;
  }
  * { box-sizing: border-box; margin: 0; padding: 0; }
  html, body {
    width: 1200px; height: 960px; overflow: hidden;
    background: var(--stage);
    font-family: "PT Sans", Arial, sans-serif;
    color: var(--ink);
  }
  .canvas { position: relative; width: 1200px; height: 960px; }

  .card {
    position: absolute;
    background: var(--card);
    box-shadow: 0 8px 22px rgba(0,0,0,0.28);
    overflow: hidden;
  }
  .card--front { left: 52px; top: 64px; width: 778px; height: 445px; z-index: 2; }
  .card--back  { left: 392px; top: 500px; width: 780px; height: 440px; z-index: 1; }

  .tagline-band { display: flex; height: 67px; }
  .tagline-band span {
    flex: 1;
    display: flex; align-items: center; justify-content: center;
    font-family: "Orbitron", "Arial Black", sans-serif;
    font-weight: 700;
    font-size: 28px; letter-spacing: 3px;
    color: var(--on-color);
  }
  .tagline-band .design  { background: var(--blue); }
  .tagline-band .develop { background: var(--green); }
  .tagline-band .deploy  { background: var(--yellow); }

  .brand {
    position: absolute; left: 28px; top: 128px;
    display: flex; align-items: center; gap: 14px;
  }
  .brand__dot {
    flex: none; width: 52px; height: 52px; border-radius: 50%;
    background: var(--yellow);
  }
  .brand__name { font-size: 44px; font-weight: 400; color: var(--ink); line-height: 1; }

  .holder { position: absolute; right: 32px; top: 118px; text-align: right; }
  .holder__name { font-size: 36px; font-weight: 700; color: var(--blue); line-height: 1.1; }
  .holder__title { font-size: 29px; font-weight: 700; font-style: italic; color: var(--green); line-height: 1.2; }

  .office { position: absolute; font-size: 20px; line-height: 25px; }
  .office__city { font-weight: 700; }
  .card--front .office { top: 262px; }
  .card--front .office--atlanta  { left: 300px; }
  .card--front .office--savannah { left: 548px; }

  .email {
    position: absolute; font-size: 20px; line-height: 25px; color: var(--blue);
  }
  .card--front .email { left: 300px; top: 342px; }

  .card--back .office { top: 100px; font-size: 19.5px; line-height: 24.5px; }
  .card--back .office--atlanta  { right: 418px; text-align: right; }
  .card--back .office--savannah { left: 432px; }
  .card--back .email { left: 0; right: 0; top: 300px; text-align: center; }

  .web-bar {
    position: absolute; left: 0; right: 0; bottom: 0;
    height: 68px; background: var(--footer);
    border-top: 4px solid var(--blue);
    display: flex; align-items: center; justify-content: center;
    font-size: 32px; color: var(--ink); letter-spacing: 0.3px;
  }
</style>
</head>
<body>
<main class="canvas">

  <section class="card card--front" aria-label="Business card front">
    <div class="tagline-band">
      <span class="design">DESIGN</span>
      <span class="develop">DEVELOP</span>
      <span class="deploy">DEPLOY</span>
    </div>

    <div class="brand">
      <span class="brand__dot"></span>
      <span class="brand__name">Quelvane<br>Systems, Inc.</span>
    </div>

    <div class="holder">
      <p class="holder__name">Marla Dunstead</p>
      <p class="holder__title">CEO</p>
    </div>

    <div class="office office--atlanta">
      <p class="office__city">Atlanta :</p>
      <p>Office: 404.555.0182</p>
      <p>Fax: 404.555.0147</p>
    </div>
    <div class="office office--savannah">
      <p class="office__city">Savannah:</p>
      <p>Office: 912.555.0139</p>
      <p>Fax: 404.555.0147</p>
    </div>

    <p class="email">mdunstead@quelvanesystems.example</p>

    <div class="web-bar">www.quelvanesystems.example</div>
  </section>

  <section class="card card--back" aria-label="Business card back">
    <div class="tagline-band">
      <span class="design">DESIGN</span>
      <span class="develop">DEVELOP</span>
      <span class="deploy">DEPLOY</span>
    </div>

    <div class="office office--atlanta">
      <p class="office__city">Atlanta Address:</p>
      <p>87 Corliss Avenue, #2291</p>
      <p>Atlanta, GA 30301</p>
      <p>Office: 404.555.0182</p>
      <p>Fax: 404.555.0147</p>
    </div>
    <div class="office office--savannah">
      <p class="office__city">Savannah Address:</p>
      <p>350 West Harrow Bend Road</p>
      <p>Suite 720</p>
      <p>Savannah, GA 31401</p>
      <p>Office: 912.555.0139</p>
      <p>Fax: 404.555.0147</p>
    </div>

    <p class="email">mdunstead@quelvanesystems.example</p>

    <div class="web-bar">www.quelvanesystems.example</div>
  </section>

</main>
</body>
</html>
```